Business Card Design

I want a non fussy clear design. I like Vintage, Retro writing for the main name as it will be a banner for the roof sign.
Company name, address and ph no. I would also like a unisex symbol small in the corner of the card. The colour of the card does not have to be blue. But I do want a bright clean clear card. A head sillohette small in the other corner possibly.

Industry/Entity Type

Business

Contact Information for Business Card

Zet Hair Design
318 Kellaby Road, Kellaby
Ph (09) 4162903

Requirements
Must have
• The back of the card must have appointment time, date dont worry about the location as its obviously on the front of the card

```html
<!DOCTYPE html>
<html lang="en">
<head>
<meta charset="utf-8">
<title>Zet Hair Design – Business Card</title>
<link rel="stylesheet" href="https://fonts.googleapis.com/css2?family=Open+Sans:wght@600;700&display=swap">
<style>
  :root {
    --page-bg: #e9ecf1;
    --card-white: #ffffff;
    --brand-blue: #1b74b8;
    --band-navy: #0e2a5c;
    --ink-navy: #13305f;
    --rule-grey: #4a4f5a;
    --text-light: #ffffff;
    --shadow: rgba(10, 30, 60, 0.22);
  }
  * { box-sizing: border-box; margin: 0; padding: 0; }
  html, body {
    width: 1200px;
    height: 848px;
    overflow: hidden;
  }
  body {
    background: var(--page-bg);
    font-family: "Open Sans", Arial, sans-serif;
    position: relative;
  }
  .card {
    position: absolute;
    top: 264px;
    width: 520px;
    height: 320px;
    border-radius: 22px;
    background: var(--card-white);
    box-shadow: 0 10px 28px var(--shadow);
    overflow: hidden;
  }

  /* Front */
  .card--front { left: 50px; }
  .front__brand {
    position: absolute;
    left: 0; top: 0;
    width: 100%;
    height: 178px;
  }
  .brand-mark {
    position: absolute;
    left: 42px;
    top: 48px;
    width: 82px;
    height: 82px;
    border-radius: 50%;
    background: var(--brand-blue);
  }
  .brand-name {
    position: absolute;
    left: 170px;
    top: 26px;
    color: var(--brand-blue);
    font-weight: 600;
    text-transform: uppercase;
    line-height: 1;
  }
  .brand-name__main {
    display: block;
    font-size: 72px;
    letter-spacing: 1px;
  }
  .brand-name__sub {
    display: block;
    font-size: 30px;
    letter-spacing: 27px;
    margin-top: 14px;
    padding-left: 20px;
  }
  .front__band {
    position: absolute;
    left: 0; bottom: 0;
    width: 100%;
    height: 142px;
    background: var(--band-navy);
    color: var(--text-light);
  }
  .contact {
    position: absolute;
    left: 44px;
    top: 30px;
    font-weight: 600;
    font-size: 17px;
    text-transform: uppercase;
    letter-spacing: 0.4px;
    line-height: 1.6;
  }
  .contact__phone { display: block; padding-left: 96px; }

  /* Back */
  .card--back { left: 630px; }
  .appointment {
    position: absolute;
    left: 48px;
    top: 54px;
    width: 424px;
  }
  .appointment__title {
    text-align: center;
    color: var(--ink-navy);
    font-weight: 700;
    font-size: 24px;
    letter-spacing: 1.5px;
    margin-bottom: 28px;
    padding-left: 20px;
  }
  .field-row {
    display: flex;
    align-items: flex-end;
    gap: 6px;
    height: 34px;
    color: var(--ink-navy);
    font-weight: 600;
    font-size: 15px;
    letter-spacing: 0.5px;
  }
  .field-row__rule {
    flex: 1;
    border-bottom: 1.5px solid var(--rule-grey);
    margin-bottom: 4px;
  }
  .field-row__label--inline { margin-left: 6px; }
  .back__brand {
    position: absolute;
    left: 0;
    width: 100%;
    bottom: 34px;
    display: flex;
    justify-content: center;
    align-items: center;
    gap: 12px;
  }
  .back__brand-mark {
    width: 48px;
    height: 48px;
    border-radius: 50%;
    background: var(--brand-blue);
  }
  .back__brand-name {
    color: var(--brand-blue);
    font-weight: 600;
    font-size: 22px;
    text-transform: uppercase;
    letter-spacing: 1px;
  }
</style>
</head>
<body>

  <section class="card card--front" aria-label="Business card front">
    <div class="front__brand">
      <span class="brand-mark" aria-hidden="true"></span>
      <h1 class="brand-name">
        <span class="brand-name__main">Zet Hair</span>
        <span class="brand-name__sub">Design</span>
      </h1>
    </div>
    <div class="front__band">
      <p class="contact">
        <span class="contact__address">318 Kellaby Road, Kellaby</span>
        <span class="contact__phone">Phone: (09) 4162903</span>
      </p>
    </div>
  </section>

  <section class="card card--back" aria-label="Business card back">
    <div class="appointment">
      <h2 class="appointment__title">APPOINTMENT</h2>
      <div class="field-row">
        <span class="field-row__label">NAME:</span>
        <span class="field-row__rule"></span>
      </div>
      <div class="field-row">
        <span class="field-row__label">DATE:</span>
        <span class="field-row__rule"></span>
        <span class="field-row__label field-row__label--inline">TIME:</span>
        <span class="field-row__rule"></span>
      </div>
    </div>
    <div class="back__brand">
      <span class="back__brand-mark" aria-hidden="true"></span>
      <span class="back__brand-name">Zet Hair Design</span>
    </div>
  </section>

</body>
</html>
```